Velmora Water Purification

We need a website set up on a "Free account" WordPress platform. (This is the type of Wordpress site that you can sign up for and create online for free (not a server-hosted type.)
The website will be for a water purification company. They install devices in homes to purify the water for safer drinking, bathing, and cleaning.
Our logo is attached. Please keep color scheme of the website consistent with the logo.
Water Purification

```html
<!DOCTYPE html>
<html lang="en">
<head>
<meta charset="utf-8">
<title>Velmora Water Purification</title>
<link rel="stylesheet" href="https://fonts.googleapis.com/css2?family=Roboto+Condensed:wght@400;700&family=Open+Sans:wght@400;600&display=swap">
<style>
:root{
  --blue:#2a87b9;
  --blue-band:#2b8bbd;
  --ink:#2b2b2b;
  --ink-soft:#4a4f54;
  --text:#6a6a6a;
  --nav:#2f2f2f;
  --nav-line:#454545;
  --btn:#474d52;
  --footer:#2e2e2e;
  --footer-bar:#222222;
  --footer-text:#9a9a9a;
  --rule:#d9d9d9;
  --white:#ffffff;
}
*{box-sizing:border-box;margin:0;padding:0}
html,body{width:1200px;height:2222px;overflow:hidden;background:var(--white)}
body{position:relative;font-family:"Open Sans",Arial,sans-serif;color:var(--text)}
.cond{font-family:"Roboto Condensed","Arial Narrow",sans-serif}
.abs{position:absolute}

/* header */
.site-header{position:absolute;left:0;top:0;width:1200px;height:89px}
.brand{position:absolute;left:160px;top:22px;display:flex;align-items:center;gap:10px}
.brand-dot{width:36px;height:36px;border-radius:50%;background:var(--blue)}
.brand-name{font-family:"Roboto Condensed",sans-serif;font-weight:700;font-size:30px;color:var(--blue)}
.contact-label{position:absolute;left:712px;top:37px;font-size:13px;color:var(--blue)}
.phone-pill{position:absolute;left:852px;top:30px;width:186px;height:34px;border:1px solid var(--rule);border-radius:17px;
  font-size:13px;font-weight:600;color:var(--ink);line-height:32px;padding-left:14px}
.phone-pill .call{position:absolute;right:0;top:0;width:32px;height:32px;border-radius:50%;background:var(--ink);display:flex;align-items:center;justify-content:center}

/* nav */
.main-nav{position:absolute;left:0;top:89px;width:1200px;height:37px;background:var(--nav)}
.main-nav ul{list-style:none;position:absolute;left:160px;top:0;display:flex;height:37px}
.main-nav li{height:37px;border-right:1px solid var(--nav-line);color:var(--white);font-size:11px;line-height:37px;text-align:center;text-transform:uppercase}
.main-nav .home{width:59px;background:var(--blue);display:flex;align-items:center;justify-content:center}

/* hero */
.hero{position:absolute;left:0;top:126px;width:1200px;height:507px;
  background:radial-gradient(ellipse at 40% 45%,#4cb4e6 0%,#1f86c4 40%,#0f4f7c 75%,#153242 100%)}
.hero-caption{position:absolute;left:0;bottom:0;width:1200px;height:88px;background:rgba(205,212,216,.82);
  display:flex;align-items:center;justify-content:center;text-align:center;
  font-family:"Roboto Condensed",sans-serif;font-weight:700;font-size:20px;line-height:25px;color:#151515;text-transform:uppercase}

/* welcome */
.welcome-title{position:absolute;left:160px;top:680px;font-family:"Roboto Condensed",sans-serif;font-weight:700;font-size:47px;line-height:51px;color:var(--blue)}
.welcome-sub{position:absolute;left:160px;top:787px;font-family:"Roboto Condensed",sans-serif;font-weight:700;font-size:26px;color:var(--ink-soft)}
.welcome-copy{position:absolute;left:464px;top:684px;width:580px}
.welcome-copy h3{font-family:"Roboto Condensed",sans-serif;font-weight:700;font-size:14px;color:var(--ink);margin-bottom:8px}
.welcome-copy p{font-size:11.5px;line-height:17px;color:var(--text)}
.btn{display:block;background:var(--btn);color:var(--white);font-family:"Roboto Condensed",sans-serif;font-weight:700;text-transform:uppercase;text-align:center;border-radius:3px}
.btn-lg{position:absolute;left:464px;top:764px;width:207px;height:49px;line-height:49px;font-size:15px}
.rule{position:absolute;left:160px;top:861px;width:881px;height:2px;background:var(--rule)}

/* features */
.feature{position:absolute;top:904px;width:260px}
.feature svg{position:absolute;left:0;top:6px}
.feature h4{margin-left:52px;font-family:"Roboto Condensed",sans-serif;font-weight:700;font-size:15px;color:var(--ink);text-transform:uppercase}
.feature p{margin-left:52px;margin-top:6px;font-size:11px;line-height:16px;color:var(--text);width:200px}

/* services band */
.services{position:absolute;left:0;top:1050px;width:1200px;height:506px;background:var(--blue-band)}
.section-title{position:absolute;left:0;width:1200px;text-align:center;font-family:"Roboto Condensed",sans-serif;font-weight:700;font-size:31px}
.services .section-title{top:50px;color:var(--white)}
.card{position:absolute;top:111px;width:271px;height:332px;background:var(--white)}
.card-media{height:157px}
.card h4{margin:26px 24px 0;font-family:"Roboto Condensed",sans-serif;font-weight:700;font-size:15px;color:var(--ink);text-transform:uppercase}
.card p{margin:10px 24px 0;font-size:11px;line-height:16px;color:var(--text)}
.btn-sm{position:absolute;left:24px;top:273px;width:83px;height:32px;line-height:32px;font-size:10px;font-weight:400}

/* products */
.products .section-title{top:1602px;color:var(--ink-soft)}
.product-strip{position:absolute;left:160px;top:1667px;width:881px;height:177px;display:flex}
.product-strip div{flex:1}
.pager{position:absolute;top:1879px;width:28px;height:28px;border-radius:3px;font-size:12px;font-weight:600;line-height:26px;text-align:center}
.pager.active{left:566px;background:var(--btn);color:var(--white);border:1px solid var(--btn)}
.pager.idle{left:606px;background:var(--white);color:var(--ink);border:1px solid #bdbdbd}

/* footer */
.site-footer{position:absolute;left:0;top:1963px;width:1200px;height:222px;background:var(--footer)}
.footer-brand{position:absolute;left:160px;top:10px;width:148px;height:91px;background:var(--white);display:flex;align-items:center;justify-content:center;gap:8px}
.footer-brand .brand-dot{width:26px;height:26px}
.footer-brand .brand-name{font-size:24px}
.footer-about{position:absolute;left:160px;top:113px;width:370px;font-size:10.5px;line-height:15px;color:var(--footer-text)}
.footer-about p+p{margin-top:12px}
.footer-col h5{font-size:15px;font-weight:400;color:var(--white);margin-bottom:8px}
.quick-links{position:absolute;left:594px;top:24px}
.quick-links ul{list-style:none}
.quick-links li{font-size:10.5px;line-height:20px;color:var(--footer-text);padding-left:27px;position:relative}
.quick-links li svg{position:absolute;left:12px;top:7px}
.contact-col{position:absolute;left:770px;top:24px;width:280px}
.contact-col ul{list-style:none}
.contact-col li{font-size:10.5px;line-height:24px;color:var(--footer-text);padding-left:24px;position:relative}
.contact-col li svg{position:absolute;left:2px;top:6px}
.socials{position:absolute;left:807px;top:157px;display:flex;gap:7px}
.socials span{width:27px;height:27px;border-radius:50%;background:var(--white)}
.footer-bar{position:absolute;left:0;top:2185px;width:1200px;height:37px;background:var(--footer-bar);font-size:10.5px;color:#b5b5b5}
.footer-bar .legal{position:absolute;left:160px;top:14px}
.footer-bar .copy{position:absolute;right:160px;top:14px}
</style>
</head>
<body>

<header class="site-header">
  <div class="brand"><span class="brand-dot"></span><span class="brand-name">Velmora</span></div>
  <div class="contact-label">Contact Information</div>
  <div class="phone-pill">0044 - 555 - 010 - 77
    <span class="call"><svg width="14" height="14" viewBox="0 0 24 24"><path fill="#fff" d="M6.6 10.8a15.1 15.1 0 0 0 6.6 6.6l2.2-2.2c.3-.3.7-.4 1-.2 1.1.4 2.3.6 3.6.6.6 0 1 .4 1 1V20c0 .6-.4 1-1 1A17 17 0 0 1 3 4c0-.6.4-1 1-1h3.5c.6 0 1 .4 1 1 0 1.3.2 2.5.6 3.6.1.3 0 .7-.2 1z"/></svg></span>
  </div>
</header>

<nav class="main-nav">
  <ul>
    <li class="home"><svg width="20" height="18" viewBox="0 0 20 18"><path fill="#fff" d="M10 1 1 9h3v8h4.5v-5h3v5H16V9h3z"/></svg></li>
    <li style="width:107px">Services &nbsp;<svg width="8" height="6" viewBox="0 0 8 6"><path fill="#fff" d="M0 0h8L4 5z"/></svg></li>
    <li style="width:102px">Products</li>
    <li style="width:98px">About Us</li>
    <li style="width:107px">Contact Us</li>
  </ul>
</nav>

<section class="hero" role="img" aria-label="Hand holding a glass filled with clean water from a chrome kitchen faucet against a blue backdrop">
  <div class="hero-caption">Velmora Water Purificatio is specialist in water purification<br>and reverse osmosis</div>
</section>

<section class="welcome">
  <h1 class="welcome-title">WELCOME TO<br>VELMORA</h1>
  <div class="welcome-sub">Water Purification</div>
  <div class="welcome-copy">
    <h3>Ut enim ad minim veniam, quis nostrud exercitation</h3>
    <p>Ut enim ad minim veniam, quis nostrud exercitation ullamco laboris nisi ut aliquip ex ea commodo con-<br>sequat. Duis aute irure dolor in reprehenderit in voluptate velit esse cillum dolore eu fugiat.</p>
  </div>
  <a class="btn btn-lg">Read More</a>
  <div class="rule"></div>
</section>

<section class="features">
  <div class="feature" style="left:160px">
    <svg width="40" height="36" viewBox="0 0 40 36" fill="none" stroke="#2a87b9" stroke-width="2"><path d="M4 15 20 3l16 12M8 12v14h24V12"/><rect x="16" y="16" width="8" height="10"/><path d="M2 30c4 3 8-3 12 0s8-3 12 0 8-3 12 0M2 34c4 3 8-3 12 0s8-3 12 0 8-3 12 0"/></svg>
    <h4>Whole House Water Filters</h4>
    <p>Ut enim ad minim veniam, quis nostrud exercitation ullamco laboris nisi ut aliquip ex ea commodo conse-quat.</p>
  </div>
  <div class="feature" style="left:474px">
    <svg width="40" height="40" viewBox="0 0 40 40"><circle cx="16" cy="11" r="7" fill="#2a87b9"/><path d="M3 38c0-10 6-16 13-16s13 6 13 16z" fill="#2a87b9"/><path d="M32 4c3 4 5 7 5 9a5 5 0 0 1-10 0c0-2 2-5 5-9z" fill="#2a87b9"/></svg>
    <h4>Drinking Water Filters</h4>
    <p>Ut enim ad minim veniam, quis nostrud exercitation ullamco laboris nisi ut aliquip ex ea commodo conse-quat.</p>
  </div>
  <div class="feature" style="left:785px">
    <svg width="40" height="42" viewBox="0 0 40 42" fill="none" stroke="#2a87b9" stroke-width="2"><path d="M6 10h28l-3 30H9z"/><path d="M8 22h24"/><circle cx="16" cy="30" r="2"/><circle cx="24" cy="33" r="2"/><path d="M10 2v4M16 2v4M22 2v4M28 2v4M34 2v4"/></svg>
    <h4>Replacement Products</h4>
    <p>Ut enim ad minim veniam, quis nostrud exercitation ullamco laboris nisi ut aliquip ex ea commodo conse-quat.</p>
  </div>
</section>

<section class="services">
  <h2 class="section-title">VELMORA WATER PURIFICATION</h2>
  <article class="card" style="left:160px">
    <div class="card-media" role="img" aria-label="Glass being filled from a faucet on a blue background" style="background:linear-gradient(135deg,#1b78b8,#4fb3e3 55%,#1d6ea8)"></div>
    <h4>Specialty Water Filtration</h4>
    <p>Ut enim ad minim veniam, quis nostrud exercitation ullamco laboris nisi ut aliquip ex ea commodo</p>
    <a class="btn btn-sm">Read More</a>
  </article>
  <article class="card" style="left:464px">
    <div class="card-media" role="img" aria-label="Cup being filled at a water cooler tap" style="background:linear-gradient(135deg,#c9c9c4,#eeeeea 55%,#b9b8b2)"></div>
    <h4>Bottleless Water Coolers</h4>
    <p>Ut enim ad minim veniam, quis nostrud exercitation ullamco laboris nisi ut aliquip ex ea commodo</p>
    <a class="btn btn-sm">Read More</a>
  </article>
  <article class="card" style="left:769px">
    <div class="card-media" role="img" aria-label="Reverse osmosis filter system installed under a kitchen sink" style="background:linear-gradient(135deg,#5a4638,#b49c7a 50%,#e8e3dc)"></div>
    <h4>Reverse Osmosis Systems</h4>
    <p>Ut enim ad minim veniam, quis nostrud exercitation ullamco laboris nisi ut aliquip ex ea commodo</p>
    <a class="btn btn-sm">Read More</a>
  </article>
</section>

<section class="products">
  <h2 class="section-title">OUR PRODUCTS</h2>
  <div class="product-strip">
    <div role="img" aria-label="Industrial water treatment plant with tanks and piping" style="background:linear-gradient(135deg,#a9b4b6,#d8dcd8 50%,#8c7f6e)"></div>
    <div role="img" aria-label="Countertop water purifier units on a violet background" style="background:linear-gradient(135deg,#8a5fc4,#e6dff0 50%,#9d6fd0)"></div>
    <div role="img" aria-label="Technician in overalls installing a filter system" style="background:linear-gradient(135deg,#c9a98a,#2f5fa8 50%,#e4e2de)"></div>
  </div>
  <span class="pager active">1</span>
  <span class="pager idle">2</span>
</section>

<footer class="site-footer">
  <div class="footer-brand"><span class="brand-dot"></span><span class="brand-name">Velmora</span></div>
  <div class="footer-about">
    <p>Lorem ipsum dolor sit amet, consectetur adipiscing elit, sed do eiusmod tempor incididunt ut labore et dolore magna aliqua. Ut enim ad minim veniam, quis nostrud exercitation ullamco laboris.</p>
    <p>nisi ut aliquip ex ea commodo consequat.</p>
  </div>
  <div class="footer-col quick-links">
    <h5>Quick Links</h5>
    <ul>
      <li><svg width="5" height="7" viewBox="0 0 5 7"><path d="M0 0l5 3.5L0 7z" fill="#2a87b9"/></svg>Home</li>
      <li><svg width="5" height="7" viewBox="0 0 5 7"><path d="M0 0l5 3.5L0 7z" fill="#2a87b9"/></svg>Services</li>
      <li><svg width="5" height="7" viewBox="0 0 5 7"><path d="M0 0l5 3.5L0 7z" fill="#2a87b9"/></svg>Products</li>
      <li><svg width="5" height="7" viewBox="0 0 5 7"><path d="M0 0l5 3.5L0 7z" fill="#2a87b9"/></svg>About Us</li>
      <li><svg width="5" height="7" viewBox="0 0 5 7"><path d="M0 0l5 3.5L0 7z" fill="#2a87b9"/></svg>Contact Us</li>
    </ul>
  </div>
  <div class="footer-col contact-col">
    <h5>Contact Us</h5>
    <ul>
      <li><svg width="10" height="13" viewBox="0 0 10 13"><path fill="#777" d="M5 0a5 5 0 0 0-5 5c0 4 5 8 5 8s5-4 5-8a5 5 0 0 0-5-5zm0 7a2 2 0 1 1 0-4 2 2 0 0 1 0 4z"/></svg>Lorem ipsum dolor sit amet, consectetur adipiscin</li>
      <li><svg width="10" height="12" viewBox="0 0 24 24"><path fill="#777" d="M6.6 10.8a15.1 15.1 0 0 0 6.6 6.6l2.2-2.2c.3-.3.7-.4 1-.2 1.1.4 2.3.6 3.6.6.6 0 1 .4 1 1V20c0 .6-.4 1-1 1A17 17 0 0 1 3 4c0-.6.4-1 1-1h3.5c.6 0 1 .4 1 1 0 1.3.2 2.5.6 3.6.1.3 0 .7-.2 1z"/></svg>Phone:00 5550 1987</li>
      <li><svg width="13" height="11" viewBox="0 0 13 11"><path fill="#777" d="M3 0h6v3H3zM0 4h13v5h-2v2H2V9H0zm3 3v3h7V7z"/></svg>Fax:00 5550 1988</li>
      <li><svg width="12" height="9" viewBox="0 0 12 9"><path fill="#777" d="M0 0h12v9H0zm1 1 5 4 5-4z"/></svg>Email: info@velmora.com</li>
    </ul>
  </div>
  <div class="socials" aria-label="Social links"><span></span><span></span><span></span><span></span><span></span></div>
</footer>
<div class="footer-bar">
  <span class="legal">Privacy Policy | Terms &amp; Conditions</span>
  <span class="copy">©2017 Velmora. Allrights are Reserved.</span>
</div>

</body>
</html>
```